Soho based IT support firm flyer.

We need a flyer to boost our business. We're a tech support firm based in Soho, London and provide helpdesk and call out support to SMEs in and around London.
They'll be two flyers with the same design. One is location specific and has the copy:
-
1 Month Free IT Support!
Based in Soho, we provide expert tech support for both desktops and laptops.
We have monthly as well as pay-as-you-go plans to fit your business.
Call us now and we'll show you how we can save you up to 50% on your IT spend.
-None location based is-
1 Month Free IT Support!
We provide expert, professional tech support for both desktops and laptops.
• Dedicated full time helpdesk
• Same day onsite visits
• Proactive support with monitoring
• 98% satisfaction score*
*taken from satisfaction survey sent out on closure of every case for Oct 2011 to Oct 2012
-
The location one needs to include a map with our location marked as postcode W9K 4TP.
I'm fine with royalty photos being used within a reasonable price. Please use PixQuarry.
Our site shows our brand best. Please keep as close to this as possible.
http://brisk-byte.example
Thanks for looking.

```html
<!DOCTYPE html>
<html lang="en">
<head>
<meta charset="utf-8">
<title>BriskByte – IT Support Flyer</title>
<link href="https://fonts.googleapis.com/css2?family=PT+Sans:wght@400;700&display=swap" rel="stylesheet">
<style>
  :root {
    --green-dark: #3f8f1d;
    --green: #6cbf2a;
    --green-light: #a8dc55;
    --lime: #b7dc3c;
    --yellow: #f5e84a;
    --orange: #f7941d;
    --orange-deep: #f08a12;
    --black: #111111;
    --band: #1a1a1a;
    --grey: #d9d9d9;
    --white: #ffffff;
    --ink: #1d1d1d;
    --map-base: #ece6da;
  }
  * { margin: 0; padding: 0; box-sizing: border-box; }
  html, body { width: 847px; height: 1200px; overflow: hidden; background: var(--white); }
  body { font-family: "PT Sans", Arial, sans-serif; color: var(--ink); }
  .flyer { position: relative; width: 847px; height: 1200px; overflow: hidden; }

  .intro {
    position: absolute; left: 0; top: 0; width: 395px; height: 522px;
    background: radial-gradient(circle at 30% 25%, var(--green-light), var(--green) 45%, var(--green-dark) 100%);
    color: var(--white); text-align: center;
  }
  .brand {
    margin: 26px auto 0; width: 300px; height: 92px; background: var(--white);
    border-radius: 18px; display: flex; align-items: center; justify-content: center; gap: 12px;
  }
  .brand-name { font-size: 44px; font-weight: 700; color: var(--green); }
  .brand-dot { width: 22px; height: 22px; border-radius: 50%; background: var(--green); }
  .tagline { margin-top: 34px; font-size: 25px; line-height: 1.25; }
  .tagline .caps { font-size: 23px; letter-spacing: 0.5px; }
  .tagline .accent { color: var(--yellow); font-weight: 700; font-size: 29px; }
  .services { margin-top: 14px; font-size: 24px; line-height: 1.25; padding: 0 30px; }

  .map {
    position: absolute; left: 395px; top: 0; width: 452px; height: 522px;
    background: linear-gradient(135deg, var(--map-base), #dfe3d6 60%, #e9e2d2);
  }

  .address-band {
    position: absolute; left: 0; top: 522px; width: 847px; height: 44px;
    background: var(--band); color: var(--yellow);
    display: flex; align-items: center; justify-content: center; font-size: 24px;
  }

  .offer { position: absolute; left: 0; top: 566px; width: 428px; height: 634px; background: var(--grey); }
  .offer-headline { position: absolute; left: 0; top: 0; width: 428px; height: 266px; background: var(--white); padding: 14px 0 0 42px; }
  .offer-headline .month { font-size: 62px; line-height: 68px; color: var(--black); }
  .offer-headline .month b { font-weight: 700; }
  .offer-headline .free { font-size: 124px; line-height: 106px; font-weight: 700; color: var(--orange); }
  .offer-headline .support { font-size: 56px; line-height: 66px; color: var(--black); }
  .note {
    position: absolute; left: 30px; width: 368px; height: 112px; background: var(--white); border-radius: 16px;
    display: flex; align-items: center; justify-content: center;
    padding: 0 20px; font-size: 22px; line-height: 1.3; text-align: center;
  }
  .note-location { top: 292px; }
  .note-plans { top: 430px; }

  .savings {
    position: absolute; left: 428px; top: 566px; width: 419px; height: 634px;
    background: linear-gradient(180deg, var(--orange), var(--orange-deep)); text-align: center; color: var(--ink);
  }
  .pitch { position: absolute; left: 0; top: 30px; width: 419px; padding: 0 50px; font-size: 31px; line-height: 38px; }
  .percent { position: absolute; left: 0; top: 136px; width: 419px; font-size: 170px; line-height: 140px; font-weight: 700; letter-spacing: -3px; }
  .spend { position: absolute; left: 0; top: 276px; width: 419px; font-size: 27px; }

  .details {
    position: absolute; left: 36px; top: 326px; width: 350px; height: 270px; background: var(--lime);
    border-radius: 22px;
  }
  .details p { position: absolute; left: 0; width: 350px; }
  .details .label { top: 18px; font-size: 29px; }
  .details .phone { top: 58px; font-size: 48px; }
  .details .email { top: 120px; font-size: 24px; }
  .details .web { top: 206px; font-size: 24px; }
</style>
</head>
<body>
<main class="flyer">
  <section class="intro">
    <div class="brand">
      <span class="brand-name">BriskByte</span>
      <span class="brand-dot"></span>
    </div>
    <p class="tagline">
      <span class="caps">WE ARE ABOUT</span><br>
      <span class="accent">Friendly &amp; Reliable</span><br>
      <span class="accent">Tech Support</span>
    </p>
    <p class="services">IT Support, Consultancy and Project Management. A one stop shop for all of your business' IT needs.</p>
  </section>

  <div class="map" role="img" aria-label="Street map of Soho with the office location marked"></div>

  <div class="address-band">12-14 Lantern House Harbour Street London W9K 4TP</div>

  <section class="offer">
    <div class="offer-headline">
      <div class="month"><b>1</b> Month</div>
      <div class="free">Free</div>
      <div class="support">IT Support!</div>
    </div>
    <p class="note note-location">Based in Soho, we provide expert tech support for both desktops and laptops.</p>
    <p class="note note-plans">We have monthly as well as pay-as-you-go plans to fit your business.</p>
  </section>

  <section class="savings">
    <p class="pitch">Call us now and we'll show you how we can save you up to</p>
    <div class="percent">50%</div>
    <p class="spend">on your IT spend.</p>
    <div class="details">
      <p class="label">Our Details</p>
      <p class="phone">0200 555 0147</p>
      <p class="email">info@brisk-byte.example</p>
      <p class="web">http://brisk-byte.example/</p>
    </div>
  </section>
</main>
</body>
</html>
```